Business Cards for a law firm

Business cards for our law firm. Use our silhoette logo and OAK HARBOR - check our website (www.oakharbor-legal.com)

Contact Information for Business Card

our silhouette logo, OAK HARBOR, 800-555-0147, Dorian Kestrup, dorian@oakharbor-legal.com

Requirements
Must have
• our silhouette logo, OAK HARBOR, 800-555-0147, Dorian Kestrup, dorian@oakharbor-legal.com

```html
<!DOCTYPE html>
<html lang="en">
<head>
<meta charset="utf-8">
<title>Oak Harbor — Business Cards</title>
<link rel="stylesheet" href="https://fonts.googleapis.com/css2?family=Montserrat:wght@400;700&display=swap">
<style>
  :root {
    --backdrop: #d2d2d2;
    --paper: #efefed;
    --navy: #172a6e;
    --ink-grey: #8c8c8c;
    --white: #ffffff;
  }
  * { box-sizing: border-box; margin: 0; padding: 0; }
  html, body {
    width: 1200px;
    height: 1051px;
    overflow: hidden;
    background: var(--backdrop);
    font-family: "Montserrat", Arial, sans-serif;
  }
  .card-set {
    position: absolute;
    top: 377px;
    left: 60px;
    display: flex;
    gap: 40px;
  }
  .card {
    width: 520px;
    height: 297px;
    border-radius: 2px;
    box-shadow: 0 14px 30px rgba(0,0,0,0.18);
  }
  .card-front {
    background: var(--paper);
    display: flex;
    flex-direction: column;
    align-items: center;
    justify-content: center;
    text-align: center;
  }
  .holder-name {
    color: var(--navy);
    font-weight: 700;
    font-size: 20px;
    letter-spacing: 0.02em;
    text-transform: uppercase;
  }
  .divider {
    width: 58px;
    height: 1px;
    background: var(--navy);
    margin: 26px 0 14px;
  }
  .contact-line {
    color: var(--ink-grey);
    font-size: 13px;
    line-height: 1.45;
    letter-spacing: 0.02em;
  }
  .contact-line .domain { color: var(--navy); }
  .card-back {
    background: var(--navy);
    display: flex;
    align-items: center;
    justify-content: center;
    gap: 16px;
  }
  .brand-mark {
    width: 14px;
    height: 14px;
    background: var(--white);
  }
  .brand-name {
    color: var(--white);
    font-weight: 400;
    font-size: 24px;
    letter-spacing: 0.14em;
  }
</style>
</head>
<body>
  <main class="card-set">
    <section class="card card-front">
      <h1 class="holder-name">Dorian Kestrup</h1>
      <div class="divider"></div>
      <p class="contact-line">800-555-0147</p>
      <p class="contact-line">dorian@oakharbor-legal.com</p>
      <p class="contact-line">www.<span class="domain">oakharbor-legal</span>.com</p>
    </section>
    <section class="card card-back">
      <span class="brand-mark"></span>
      <span class="brand-name">OAK HARBOR</span>
    </section>
  </main>
</body>
</html>
```